Skin care products for Men Label design

I am looking for a designer, who can help with the label design for my new skin care products line for Men.
Modern design, with a manly feel for ecology products.
Colors that must be included:
Black and Blue (see company logo in uploaded files)

These are the measurements:

Cleanser: MM: 130 x 60

Skintonic : MM:130 x 60

Day Creme: MM 105 x 74

Target Market(s)

Men aged 25-55

Industry/Entity Type

Skin Care Product

Requirements
Must have
• Colors that must be included:

```html
<!DOCTYPE html>
<html lang="en">
<head>
<meta charset="utf-8">
<title>Stone Ridge – Men's Skin Care Label</title>
<link rel="stylesheet" href="https://fonts.googleapis.com/css2?family=Roboto:wght@500&display=swap">
<style>
  :root {
    --backdrop: #e4e4e4;
    --label-white: #f7f8f9;
    --dot-blue: #5f8fc4;
    --band-blue: #1f5fb8;
    --band-bright: #3aa0e6;
    --band-navy: #2a3548;
    --band-navy-deep: #151c2a;
    --brand-ink: #2b2b2b;
    --brand-mark: #6a93bf;
  }
  html, body {
    margin: 0;
    padding: 0;
    width: 1200px;
    height: 1000px;
    overflow: hidden;
    background: var(--backdrop);
  }
  .canvas {
    position: relative;
    width: 1200px;
    height: 1000px;
  }
  .label {
    position: absolute;
    left: 473px;
    top: 250px;
    width: 254px;
    height: 660px;
    background: var(--label-white);
    box-shadow: 0 10px 30px rgba(0, 0, 0, 0.12);
    overflow: hidden;
  }
  .label-art {
    position: absolute;
    inset: 0;
    width: 100%;
    height: 100%;
  }
  .brand {
    position: absolute;
    left: 98px;
    top: 208px;
    display: flex;
    align-items: center;
    gap: 8px;
  }
  .brand-square {
    width: 16px;
    height: 16px;
    background: var(--brand-mark);
  }
  .brand-name {
    font-family: "Roboto", sans-serif;
    font-weight: 500;
    font-size: 21px;
    color: var(--brand-ink);
    white-space: nowrap;
  }
</style>
</head>
<body>
<main class="canvas">
  <section class="label">
    <svg class="label-art" viewBox="0 0 254 660" xmlns="http://www.w3.org/2000/svg">
      <defs>
        <radialGradient id="dot-field-tone" cx="0" cy="0.55" r="0.9">
          <stop offset="0" stop-color="var(--dot-blue)" stop-opacity="0.45"/>
          <stop offset="0.6" stop-color="var(--dot-blue)" stop-opacity="0.12"/>
          <stop offset="1" stop-color="var(--dot-blue)" stop-opacity="0"/>
        </radialGradient>
        <linearGradient id="band-stripe" x1="0" y1="1" x2="1" y2="0">
          <stop offset="0" stop-color="var(--band-blue)"/>
          <stop offset="0.5" stop-color="var(--band-bright)"/>
          <stop offset="1" stop-color="var(--band-blue)"/>
        </linearGradient>
        <linearGradient id="band-base" x1="0" y1="0" x2="1" y2="0">
          <stop offset="0" stop-color="var(--band-navy-deep)"/>
          <stop offset="0.5" stop-color="var(--band-navy)"/>
          <stop offset="1" stop-color="var(--band-navy-deep)"/>
        </linearGradient>
      </defs>
      <g class="dot-field" role="img" aria-label="Halftone dot pattern sweeping in blue across the left of the label">
        <rect x="0" y="0" width="200" height="620" fill="url(#dot-field-tone)"/>
      </g>
      <path class="band-stripe" d="M0 585 L254 420 L254 452 L0 640 Z" fill="url(#band-stripe)"/>
      <path class="band-base" d="M0 640 L254 452 L254 660 L0 660 Z" fill="url(#band-base)"/>
    </svg>
    <div class="brand">
      <span class="brand-square"></span>
      <span class="brand-name">Stone Ridge</span>
    </div>
  </section>
</main>
</body>
</html>
```